Brisk Sealcraft - Logo and Advert

Help to provide logo and advert.
Advert is to be short and concise to fit in a printed directory posted around homes.
Ideally the same advert to be able to be blown up as a leaflet.
Use of eco friendly type colours, soft greens and blues.
Logo to be subtle but indicative to roofing and facades.
Breakdown of advert as follows;
Company name:
Brisk Sealcraft
Sub title:
Roofing & Façades
Services breakdown:
Pitched (Slating & Tiling)
Flat (Single Ply, Liquid & Mineral Felt)
Hard Metal (Zinc Standing Seam)
Leadwork
Roof lights and lanterns
Generic notes:
100% flame free applications available, eliminating all fire risks to your property. (No gas torch’s etc.).
Expert consultation and advice.
Product warranty and/or insurance backed warranty available.
Fully insured contractor.
Contact information:
Phone number to be confirmed
Email and/or website to be confirmed.
Please feel free to try out different colours and fonts other than outlined. I am not limited to those and open to suggestions.
Updates
Target Market(s)
Domestic/Private Home Owners/Small Buidlers
Industry/Entity Type
Roofing
Font styles to use
Look and feel
Each slider illustrates characteristics of the customer's brand and the style your logo design should communicate.

```html
<!DOCTYPE html>
<html lang="en">
<head>
<meta charset="utf-8">
<title>Brisk Sealcraft – Roofing &amp; Façades</title>
<link href="https://fonts.googleapis.com/css2?family=Michroma&family=Roboto+Condensed:wght@400;700&family=Roboto:wght@400&display=swap" rel="stylesheet">
<style>
  :root {
    --white: #ffffff;
    --blue: #0a93d2;
    --lime: #b6d53c;
    --dark: #111214;
    --slate: #5f6b73;
    --brick: #9a6450;
    --sky: #e9eef0;
  }
  * { margin: 0; padding: 0; box-sizing: border-box; }
  html, body { width: 872px; height: 1200px; overflow: hidden; background: var(--white); }
  .advert { position: relative; width: 872px; height: 1200px; background: var(--white); font-family: "Roboto Condensed", sans-serif; }

  .hero { position: absolute; left: 0; top: 0; width: 872px; height: 528px;
    background: linear-gradient(180deg, var(--white) 0%, var(--sky) 12%, #8d969b 30%, var(--slate) 55%, var(--brick) 82%, #7e5444 100%); }
  .hero-title { position: absolute; left: 0; width: 872px; top: 266px; text-align: center; color: var(--white);
    font-family: "Michroma", sans-serif; font-size: 52px; letter-spacing: 2px; line-height: 1; white-space: nowrap; }
  .hero-sub { position: absolute; left: 54px; width: 756px; top: 330px; display: flex; align-items: center; gap: 30px;
    color: var(--white); font-family: "Michroma", sans-serif; font-size: 28px; letter-spacing: 1px; white-space: nowrap; }
  .hero-sub .rule { flex: 1; height: 2px; background: var(--white); }

  .services { position: absolute; left: 0; top: 540px; width: 872px; height: 275px; }
  .services-photo { position: absolute; left: 0; top: 0; width: 872px; height: 275px;
    background: linear-gradient(120deg, #f2f5f7 0%, #c9dbe8 25%, #3f86c7 45%, #1f5f9e 60%); }
  .services-panel { position: absolute; left: 0; top: 0; }
  .services-heading { position: absolute; left: 391px; top: 22px; color: var(--white); font-weight: 700; font-size: 42px; line-height: 1; }
  .service-list { list-style: none; position: absolute; top: 80px; left: 0; color: var(--white); font-size: 28px; line-height: 32.3px; }
  .service-list li { position: relative; white-space: nowrap; }
  .service-list li::before { content: ""; position: absolute; left: -28px; top: 11px; width: 12px; height: 12px; background: var(--white); }

  .features { position: absolute; top: 826px; left: 0; width: 872px; height: 264px; }
  .feature-side { position: absolute; top: 0; height: 264px; }
  .feature-side.left { left: 0; width: 200px; background: linear-gradient(90deg, #a9cc36, var(--lime)); }
  .feature-side.right { left: 673px; width: 199px; background: linear-gradient(135deg, #c6de6a, #a7c744); }
  .feature-center { position: absolute; left: 209px; top: 0; width: 456px; height: 264px;
    background: linear-gradient(180deg, #2c6fd0 0%, #5aa0e0 35%, #5f7b5a 62%, #6a6c6e 100%); }
  .feature-notes { position: absolute; left: 209px; top: 15px; width: 456px; text-align: center; color: var(--white);
    font-size: 20px; line-height: 23.5px; text-shadow: 0 1px 2px rgba(0,0,0,.4); }
  .feature-notes p + p { margin-top: 22.5px; }

  .footer { position: absolute; left: 0; top: 1100px; width: 872px; height: 89px; background: var(--dark); color: var(--white); }
  .footer-brand { position: absolute; left: 98px; top: 28px; width: 284px; text-align: center; }
  .footer-name { font-family: "Michroma", sans-serif; font-size: 19.5px; line-height: 1; white-space: nowrap; }
  .footer-sub { display: flex; align-items: center; gap: 12px; margin-top: 5px; font-family: "Michroma", sans-serif; font-size: 11px; white-space: nowrap; }
  .footer-sub .rule { flex: 1; height: 1px; background: var(--white); }
  .footer-mark { position: absolute; left: 52px; top: 31px; width: 28px; height: 28px; background: var(--white); }
  .footer-contact { position: absolute; top: 31px; left: 491px; display: flex; align-items: center; font-family: "Roboto", sans-serif; font-size: 16.5px; }
  .footer-contact .divider { width: 2px; height: 30px; background: var(--blue); margin: 0 12px 0 10px; }
  .base-strip { position: absolute; left: 0; top: 1189px; width: 872px; height: 11px; background: linear-gradient(90deg, #3a3a3a, #d8d8d8 50%, #3a3a3a); }
</style>
</head>
<body>
<main class="advert">
  <section class="hero" role="img" aria-label="Photograph of new houses with grey tiled pitched roofs and red brick gables">
    <h1 class="hero-title">BRISK SEALCRAFT</h1>
    <div class="hero-sub"><span class="rule"></span><span>ROOFING &amp; FAÇADES</span><span class="rule"></span></div>
  </section>

  <section class="services">
    <div class="services-photo" role="img" aria-label="Photograph of a white roofing membrane roll with water droplets"></div>
    <svg class="services-panel" width="872" height="275" viewBox="0 0 872 275" aria-hidden="true">
      <polygon points="354,0 872,0 872,275 227,275" fill="var(--blue)"/>
      <polygon points="346,0 354,0 227,275 219,275" fill="var(--white)"/>
    </svg>
    <h2 class="services-heading">SERVICES</h2>
    <ul class="service-list">
      <li style="left:383px">Pitched (Slating &amp; Tiling)</li>
      <li style="left:371px">Flat (Single Ply, Liquid &amp; Mineral Felt)</li>
      <li style="left:354px">Hard Metal (Zinc Standing Seam)</li>
      <li style="left:336px">Leadwork</li>
      <li style="left:325px">Roof lights and lanterns</li>
    </ul>
  </section>

  <section class="features">
    <div class="feature-side left" role="img" aria-label="Photograph of green standing seam metal cladding"></div>
    <div class="feature-center" role="img" aria-label="Photograph of a glazed roof lantern on a flat roof under blue sky"></div>
    <div class="feature-notes">
      <p>100% flame free applications available,<br>eliminating all fire risks to your property.<br>(No gas torch's etc.).</p>
      <p>Expert consultation and advice.</p>
      <p>Product warranty and/or insurance backed<br>warranty available.</p>
      <p>Fully insured contractor.</p>
    </div>
    <div class="feature-side right" role="img" aria-label="Photograph of a green metal roof edge detail"></div>
  </section>

  <footer class="footer">
    <span class="footer-mark"></span>
    <div class="footer-brand">
      <div class="footer-name">BRISK SEALCRAFT</div>
      <div class="footer-sub"><span class="rule"></span><span>ROOFING &amp; FAÇADES</span><span class="rule"></span></div>
    </div>
    <div class="footer-contact">
      <span>000-555-0142</span><span class="divider"></span><span>info@brisk_sealcraft.com</span>
    </div>
  </footer>
  <div class="base-strip"></div>
</main>
</body>
</html>
```